Expanding National Maid Service Needs Redesign!

We need a redesigned home page for our residential cleaning company. Winner will be recognized as the designer for a brand about to go national within the United States. Winner will also become the first choice to continue working with the company to design at least 15 more pages.

Looking for redesign of homepage and redesign of logo (logo will use the same elements -- just organized differently with horizontal text).

For the design we are looking for a mix between the following websites:
www. brigadeofsweepers .com
This is our parent site that will be redesigned

www. tidycorsairs .com
We really like the top/header having the three steps.
We would like to have the same font (proxima nova) and colors. We like the location and size of the booking form.
Love the section topics and would like to mimic that.

www. brighthavenkeepers .com
We really like the clean art and use of colors.
We love the use of b-roll and branded images. Will provide for our website.

The perfect site would have the cleanliness, layout and booking form of Tidy Corsairs and the excellent placement and use of branded images and b-roll of Bright Haven Keepers.

Link to branded images and b-roll is attached to the brief in a text file.

Please message me any questions. Good luck to everyone in the project!

Target Market(s)

Male and Female working professionals between the ages of 30-60 years old.

Industry/Entity Type

Cleaning Service

Number of Pages Required

1 page

Font styles to use
Other font styles liked:
• Proxima Nova

Colors
0355a3
add136

Requirements
Must have
• Most of this is covered in the project description.
• Would like to have our logo split up so that the art of the maids remains the same but the "Brigade of Sweepers" text is to the right of the art. Looking for it to be a horizontal logo.
• Must use Proxima Nova font.
• Must use our branded images and videos. Feel free to create stills from the video.
Nice to have
• Nice to have, but not expected, is the b-roll edited to work with your design. We would like to see the designers vision of how the video would look with the website.
• Would be nice to have our logo given an updated look. Made horizontal as mentioned in the project description.
Should not have
• Should not feel busy. Should not use different color scheme than that of Tidy Corsairs. Should not have non-branded images of maids.

```html
<!DOCTYPE html>
<html lang="en">
<head>
<meta charset="utf-8">
<title>Brigade of Sweepers – Home</title>
<link href="https://fonts.googleapis.com/css2?family=Montserrat:wght@400;500;600;700;800&family=Kaushan+Script&display=swap" rel="stylesheet">
<style>
:root{
  --blue:#0355a3;
  --blue-dark:#023f7a;
  --blue-deep:#0a3570;
  --green:#add136;
  --green-dark:#8fb324;
  --teal:#1aa39a;
  --ink:#2b3440;
  --muted:#6b7480;
  --line:#dfe3e8;
  --paper:#ffffff;
  --soft:#f3f5f7;
}
*{box-sizing:border-box;margin:0;padding:0}
html,body{width:1200px;height:4224px;overflow:hidden}
body{font-family:"Montserrat",sans-serif;color:var(--ink);background:var(--paper);font-size:14px;line-height:1.6}
.script{font-family:"Kaushan Script",cursive;color:var(--green);font-size:40px;line-height:1.1;font-weight:400}
.section-title{font-size:38px;font-weight:700;color:var(--blue-deep);letter-spacing:.5px;line-height:1.2}
.center{text-align:center}
.lead{font-size:13px;color:var(--muted);max-width:1000px;margin:16px auto 0;line-height:1.7}
.btn{display:inline-block;font-size:12px;font-weight:700;letter-spacing:1px;padding:12px 28px;text-transform:uppercase}
.btn-outline{border:2px solid var(--blue);color:var(--blue);background:#fff}
.btn-solid{background:var(--blue);color:#fff;border:2px solid var(--blue)}

/* top bar */
.topbar{height:48px;background:var(--blue);color:#fff;display:flex;align-items:center;justify-content:space-between;padding:0 60px;font-size:12px}
.topbar .contact{display:flex;gap:34px}
.topbar .social{display:flex;gap:10px}
.topbar .social span{width:26px;height:26px;border-radius:50%;background:#fff;opacity:.9;display:block}

/* header */
.header{height:112px;display:flex;align-items:center;justify-content:space-between;padding:0 60px}
.brand{display:flex;align-items:center;gap:14px;font-weight:800;color:var(--blue);font-size:24px}
.brand .mark{width:56px;height:56px;border-radius:50%;background:var(--green)}
.nav{display:flex;gap:6px}
.nav a{font-size:12px;font-weight:700;color:var(--blue-deep);padding:12px 16px;text-decoration:none}
.nav a.active{background:var(--green);color:#fff}

/* hero */
.hero{position:relative;height:648px}
.hero-photo{position:absolute;inset:0;background:linear-gradient(100deg,#f7f8f9 0%,#eef1f3 40%,#d9dfd8 60%,#c6d9a6 80%,#e8ecef 100%)}
.hero-copy{position:relative;padding:130px 0 0 70px;width:640px}
.hero-copy .script{font-size:46px}
.hero-copy h1{font-size:60px;font-weight:800;color:var(--blue);line-height:1.1;margin-top:6px}
.hero-copy p{font-size:13px;color:var(--muted);margin:22px 0 34px;max-width:560px}
.hero-copy .actions{display:flex;gap:16px}

/* info bar */
.infobar{height:120px;background:var(--blue);display:flex;justify-content:space-around;align-items:center;color:#fff}
.info{display:flex;align-items:center;gap:16px}
.info svg{flex:none}
.info h4{font-size:13px;font-weight:700;text-transform:uppercase}
.info p{font-size:11px;opacity:.85;line-height:1.5}

/* appointment */
.appointment{height:892px;padding:70px 90px 0}
.steps{position:relative;margin:60px 0 0;height:90px}
.steps .track{position:absolute;left:30px;right:30px;top:20px;height:6px;background:var(--green)}
.steps .track i{display:block;width:22%;height:100%;background:var(--blue)}
.step{position:absolute;top:0;width:120px;margin-left:-60px;text-align:center}
.step .dot{width:46px;height:46px;border-radius:50%;background:var(--green);margin:0 auto;display:flex;align-items:center;justify-content:center}
.step.active .dot{background:var(--blue)}
.step span{display:block;font-size:12px;font-weight:600;color:var(--green-dark);margin-top:8px}
.step.active span{color:var(--blue)}
.note{font-size:12px;color:var(--muted);margin:30px 0 34px}
.form-row{display:grid;grid-template-columns:repeat(4,1fr);gap:30px;margin-bottom:30px}
.field label{display:block;font-size:12px;font-weight:600;margin-bottom:8px}
.field .box{height:40px;border:1px solid var(--line);display:flex;align-items:center;justify-content:space-between;padding:0 12px;font-size:12px;color:var(--muted)}
.field .box::after{content:"";width:0;height:0;border-left:5px solid transparent;border-right:5px solid transparent;border-top:6px solid var(--muted)}
.form-row.second{grid-template-columns:210px 1fr 130px 130px;align-items:end}
.days{display:flex;gap:20px;justify-content:center}
.day{text-align:center;font-size:12px;font-weight:600}
.day i{display:block;width:16px;height:16px;border:1px solid var(--muted);margin:8px auto 10px}
.next-row{text-align:right;margin-top:20px}

/* why */
.why{height:640px;background:linear-gradient(135deg,var(--green) 0%,#9cc52b 100%);padding:70px 90px 0;color:#fff}
.why .script{color:#fff}
.why .section-title{color:#fff}
.why-body{display:flex;justify-content:space-between;margin-top:60px}
.why-text{width:560px}
.why-text h3{font-size:22px;font-weight:700;line-height:1.35;margin-bottom:24px}
.why-text li{list-style:none;display:flex;gap:14px;font-size:12px;margin-bottom:16px;align-items:flex-start}
.why-text li svg{flex:none;margin-top:1px}
.video{width:400px;height:270px;background:linear-gradient(135deg,#3d5e1a,#6d8f2e 55%,#2c4212);position:relative;border:6px solid #fff}
.video .play{position:absolute;left:50%;top:50%;width:64px;height:64px;margin:-32px 0 0 -32px;border-radius:50%;background:rgba(255,255,255,.85)}
.video .play::after{content:"";position:absolute;left:26px;top:20px;border-left:18px solid var(--blue);border-top:12px solid transparent;border-bottom:12px solid transparent}

/* prices */
.prices{height:640px;padding:70px 90px 0;position:relative}
.cards{display:grid;grid-template-columns:repeat(4,1fr);gap:30px;margin-top:50px;padding:0 20px}
.card{border:1px solid var(--line);text-align:center;background:#fff}
.card .head{color:#fff;padding:18px 0 16px}
.card .head h4{font-size:18px;font-weight:700}
.card .head strong{display:block;font-size:40px;line-height:1.1;font-weight:800}
.card .head small{font-size:12px}
.card .body{padding:30px 0 24px;font-size:12px;color:var(--muted)}
.card .body .btn{margin-top:22px;padding:8px 22px;font-size:11px;letter-spacing:.5px;text-transform:none}
.c1 .head{background:var(--blue-deep)} .c1 .btn{background:var(--blue-deep);border-color:var(--blue-deep)}
.c2 .head{background:var(--blue)}
.c3 .head{background:var(--teal)} .c3 .btn{background:var(--teal);border-color:var(--teal)}
.c4 .head{background:var(--green-dark)} .c4 .btn{background:var(--green-dark);border-color:var(--green-dark)}
.arrow{position:absolute;top:388px}
.arrow.left{left:40px}.arrow.right{right:40px}

/* testimonials */
.testimonials{height:580px;position:relative;padding-top:70px}
.testi-photo{position:absolute;inset:0;background:linear-gradient(180deg,#f4f5f6 0%,#e2e4e6 50%,#d3d6d9 100%)}
.testimonials .inner{position:relative}
.avatar{width:84px;height:84px;border-radius:50%;background:#c3c8cd;border:4px solid #fff;margin:40px auto 20px}
.quote{font-size:13px;color:var(--muted);max-width:900px;margin:0 auto;font-style:italic}
.who{font-size:13px;font-weight:700;color:var(--ink);margin-top:18px}
.dots{display:flex;gap:8px;justify-content:center;margin-top:22px}
.dots i{width:10px;height:10px;border-radius:50%;background:#b8bec4}
.dots i.on{background:var(--blue)}

/* press */
.press{height:190px;background:var(--blue);color:#fff;text-align:center;padding-top:36px}
.press h3{font-size:22px;font-weight:600;letter-spacing:.5px}
.badges{display:flex;justify-content:center;gap:50px;margin-top:34px}
.badges span{width:190px;height:40px;background:rgba(255,255,255,.85);border-radius:4px}

/* footer */
.footer{height:300px;background:var(--soft);display:grid;grid-template-columns:340px 200px 240px 1fr;gap:40px;padding:40px 60px 0}
.footer .brand{font-size:20px}
.footer .brand .mark{width:44px;height:44px}
.footer h5{font-size:13px;font-weight:700;color:var(--blue-deep);margin:20px 0 8px;text-transform:uppercase}
.footer .col h5{margin-top:6px}
.footer p,.footer li{font-size:11px;color:var(--muted);line-height:1.7;list-style:none}
.footer li{padding:5px 0;border-bottom:1px solid var(--line)}
.footer .contact-line{display:flex;gap:10px;margin-bottom:12px;font-size:11px;color:var(--muted)}
.bottombar{height:54px;background:#e6e9ec;display:flex;justify-content:space-between;align-items:center;padding:0 60px;font-size:11px;color:var(--muted)}
.bottombar nav{display:flex;gap:18px}
</style>
</head>
<body>

<div class="topbar">
  <div class="contact">
    <span>(407) 555-0198</span>
    <span>hello@brigadeofsweepers.com</span>
  </div>
  <div class="social"><span></span><span></span><span></span><span></span></div>
</div>

<header class="header">
  <div class="brand"><span class="mark"></span>Brigade of Sweepers</div>
  <nav class="nav">
    <a class="active">HOME</a><a>MAID SERVICES</a><a>GIFT CARDS</a><a>ABOUT US</a><a>BLOG</a><a>CONTACT US</a>
  </nav>
</header>

<section class="hero">
  <div class="hero-photo" role="img" aria-label="Branded photo of a smiling maid in a green uniform wiping a table with a spray bottle"></div>
  <div class="hero-copy">
    <div class="script">Super Maid Service with</div>
    <h1>ECO FRIENDLY PRODUCTS</h1>
    <p>Our trained maids clean your home with safe, natural products. We treat every room with care, so you can come back to a fresh, healthy home at the end of a long working day.</p>
    <div class="actions"><span class="btn btn-outline">Know More</span><span class="btn btn-solid">Quick Quote</span></div>
  </div>
</section>

<section class="infobar">
  <div class="info">
    <svg width="46" height="46" viewBox="0 0 46 46"><circle cx="23" cy="23" r="21" fill="none" stroke="#fff" stroke-width="3"/><path d="M23 11v13l8 5" stroke="#fff" stroke-width="3" fill="none" stroke-linecap="round"/></svg>
    <div><h4>Opening Hours</h4><p>Mon – Fri 7:00am – 6:00pm<br>Saturday 9:00am – 3:00pm</p></div>
  </div>
  <div class="info">
    <svg width="36" height="46" viewBox="0 0 36 46"><path d="M18 2C9 2 3 9 3 17c0 11 15 27 15 27s15-16 15-27C33 9 27 2 18 2z" fill="#fff"/><circle cx="18" cy="17" r="6" fill="var(--blue)"/></svg>
    <div><h4>Our Location</h4><p>4180 Lantern Park Road<br>Winter Ridge, FL 32899</p></div>
  </div>
  <div class="info">
    <svg width="46" height="46" viewBox="0 0 46 46"><circle cx="23" cy="23" r="21" fill="#fff"/><path d="M13 23l7 7 13-14" stroke="var(--blue)" stroke-width="4" fill="none" stroke-linecap="round"/></svg>
    <div><h4>Guaranteed of Service</h4><p>100% Satisfaction Guarantee</p></div>
  </div>
</section>

<section class="appointment">
  <div class="center">
    <div class="script">24 Hours Support</div>
    <h2 class="section-title">MAKE AN APPOINTMENT</h2>
    <p class="lead">Book your cleaning in a few easy steps. Choose a service, pick a time that suits your schedule, and tell us about your home. Our team confirms every booking quickly, and you can change or cancel at any time before the visit.</p>
  </div>
  <div class="steps">
    <div class="track"><i></i></div>
    <div class="step active" style="left:3%"><div class="dot"><svg width="18" height="18"><circle cx="9" cy="9" r="6" fill="#fff"/></svg></div><span>1. Service</span></div>
    <div class="step" style="left:26%"><div class="dot"><svg width="18" height="18"><circle cx="9" cy="9" r="7" fill="none" stroke="#fff" stroke-width="2"/><path d="M9 5v4l3 2" stroke="#fff" stroke-width="2" fill="none"/></svg></div><span>2. Time</span></div>
    <div class="step" style="left:50%"><div class="dot"><svg width="18" height="18"><rect x="3" y="3" width="12" height="12" fill="none" stroke="#fff" stroke-width="2"/></svg></div><span>3. Details</span></div>
    <div class="step" style="left:74%"><div class="dot"><svg width="18" height="18"><rect x="2" y="5" width="14" height="9" fill="#fff"/></svg></div><span>4. Payment</span></div>
    <div class="step" style="left:97%"><div class="dot"><svg width="18" height="18"><path d="M3 9l4 4 8-8" stroke="#fff" stroke-width="2.5" fill="none"/></svg></div><span>5. Done</span></div>
  </div>
  <p class="note">Please select service. (Extras and Options are Needed and Paid for when you drop your vehicle off)</p>
  <div class="form-row">
    <div class="field"><label>Category</label><div class="box">Select Category</div></div>
    <div class="field"><label>Service</label><div class="box">Select Service</div></div>
    <div class="field"><label>Employee</label><div class="box">Any</div></div>
    <div class="field"><label>No. of persons</label><div class="box">1</div></div>
  </div>
  <div class="form-row second">
    <div class="field"><label>I'm available on or after</label><div class="box">December 10th, 2016</div></div>
    <div class="days">
      <div class="day">Mon<i></i></div><div class="day">Tue<i></i></div><div class="day">Wed<i></i></div><div class="day">Thu<i></i></div><div class="day">Fri<i></i></div><div class="day">Sat<i></i></div><div class="day">Sun<i></i></div>
    </div>
    <div class="field"><label>Start from</label><div class="box">8:00 am</div></div>
    <div class="field"><label>Finish by</label><div class="box">6:00 pm</div></div>
  </div>
  <div class="next-row"><span class="btn btn-solid">Next</span></div>
</section>

<section class="why">
  <div class="center">
    <div class="script">Why Choose Us</div>
    <h2 class="section-title">BEST CLEANING COMPANY IN THE COUNTRY</h2>
  </div>
  <div class="why-body">
    <div class="why-text">
      <h3>Fighting the war on dirt with eco-friendly weapons.</h3>
      <ul>
        <li><svg width="18" height="18"><circle cx="9" cy="9" r="9" fill="#fff"/><path d="M5 9l3 3 5-6" stroke="var(--green-dark)" stroke-width="2" fill="none"/></svg>Your friends and family will love how clean your home looks and smells.</li>
        <li><svg width="18" height="18"><circle cx="9" cy="9" r="9" fill="#fff"/><path d="M5 9l3 3 5-6" stroke="var(--green-dark)" stroke-width="2" fill="none"/></svg>Let us handle the cleaning so you can focus on what matters most.</li>
        <li><svg width="18" height="18"><circle cx="9" cy="9" r="9" fill="#fff"/><path d="M5 9l3 3 5-6" stroke="var(--green-dark)" stroke-width="2" fill="none"/></svg>Every visit is quick, flexible, friendly and affordable.</li>
        <li><svg width="18" height="18"><circle cx="9" cy="9" r="9" fill="#fff"/><path d="M5 9l3 3 5-6" stroke="var(--green-dark)" stroke-width="2" fill="none"/></svg>Backed by our unique 100% Guarantee. You have nothing to lose.</li>
      </ul>
    </div>
    <div class="video" role="img" aria-label="Branded promotional video still with play button">
      <span class="play"></span>
    </div>
  </div>
</section>

<section class="prices">
  <div class="center">
    <div class="script">Full-service house cleaning</div>
    <h2 class="section-title">PRICES &amp; PLANS</h2>
    <p class="lead">Simple, honest pricing for every home size. Every plan includes dusting, vacuuming, mopping, kitchen and bathroom care, plus the eco-friendly products our customers love. Pick a plan and book online in minutes.</p>
  </div>
  <svg class="arrow left" width="20" height="36"><path d="M16 2L4 18l12 16" stroke="#9aa2ab" stroke-width="3" fill="none"/></svg>
  <svg class="arrow right" width="20" height="36"><path d="M4 2l12 16L4 34" stroke="#9aa2ab" stroke-width="3" fill="none"/></svg>
  <div class="cards">
    <div class="card c1"><div class="head"><h4>Basic</h4><strong>$85</strong><small>per month</small></div><div class="body">One bedroom home<br><span class="btn btn-solid">Purchase</span></div></div>
    <div class="card c2"><div class="head"><h4>Standard</h4><strong>$90</strong><small>per month</small></div><div class="body">Two bedroom home<br><span class="btn btn-solid">Purchase</span></div></div>
    <div class="card c3"><div class="head"><h4>Ultimate</h4><strong>$105</strong><small>per month</small></div><div class="body">Three bedroom home<br><span class="btn btn-solid">Purchase</span></div></div>
    <div class="card c4"><div class="head"><h4>Gold</h4><strong>$120</strong><small>per month</small></div><div class="body">Four bedroom home<br><span class="btn btn-solid">Purchase</span></div></div>
  </div>
</section>

<section class="testimonials">
  <div class="testi-photo" role="img" aria-label="Soft greyscale branded photo of a maid giving a thumbs up"></div>
  <div class="inner center">
    <div class="script">Our Customers Say</div>
    <h2 class="section-title">TESTIMONIALS</h2>
    <div class="avatar" role="img" aria-label="Customer portrait"></div>
    <p class="quote">"I just wanted to thank you for your team for getting my house so clean. I came home after a week of business travel and it was spotless. The team was friendly, on time and careful with everything. I have already told all of my neighbours about you!"</p>
    <div class="who">Jenna Whitfield</div>
    <div class="dots"><i class="on"></i><i></i><i></i></div>
  </div>
</section>

<section class="press">
  <h3>WE HAVE BEEN FEATURED IN THESE PUBLICATIONS</h3>
  <div class="badges"><span></span><span></span><span></span><span></span></div>
</section>

<footer class="footer">
  <div>
    <div class="brand"><span class="mark"></span>Brigade of Sweepers</div>
    <h5>Service Areas</h5>
    <p>Winter Ridge, Lantern Park, Cedar Bay, Oak Hollow, Pine Crest, Maple Shore, Harbor Point, Willow Glen, Stone Creek, Fairview Heights and surrounding neighbourhoods.</p>
  </div>
  <div class="col">
    <h5>Navigation</h5>
    <ul><li>Home</li><li>Gift Cards</li><li>About Us</li><li>Blog</li><li>Contact Us</li></ul>
  </div>
  <div class="col">
    <h5>Services</h5>
    <ul><li>First Cleaning and Deep Clean</li><li>Weekly Maid Service</li><li>Move In/Out Cleaning</li></ul>
  </div>
  <div class="col">
    <div class="contact-line"><svg width="12" height="16"><path d="M6 0C3 0 0 2.5 0 6c0 4 6 10 6 10s6-6 6-10c0-3.5-3-6-6-6z" fill="var(--blue)"/></svg>4180 Lantern Park Road<br>Winter Ridge, FL 32899</div>
    <div class="contact-line"><svg width="14" height="12"><rect width="14" height="12" fill="var(--blue)"/><path d="M0 0l7 6 7-6" stroke="#fff" fill="none"/></svg>hello@brigadeofsweepers.com</div>
    <div class="contact-line"><svg width="14" height="14"><path d="M3 0l3 3-2 2c1 2 3 4 5 5l2-2 3 3-2 3C6 13 1 8 0 2z" fill="var(--blue)"/></svg>(407) 555-0198</div>
  </div>
</footer>
<div class="bottombar">
  <span>Brigade of Sweepers. All rights reserved. Copyright 2016-2017</span>
  <nav><span>FAQ</span><span>Blog</span><span>Terms of Service</span><span>Privacy Policy</span><span>Jobs</span><span>Log in</span><span>Sitemap</span></nav>
</div>

</body>
</html>
```